2 page Full Color Eye Catching Newsletter Design Needed

Our Company, Brightway Counseling, needs a front and back 8.5 x 11 newsletter, that resembles a newspaper. We are looking for a full color, clean and modern look. We are not a plain type of company. There are several articles that need to go on the newspaper. One Main article will go on the front, and the other four will go on the back of the newspaper. We also want an advertisement for our company to be on the front of the the newspaper.

We need your creativity to flow, as we would like for you to come up with a catchy name for our newspaper. I have attached some sample newspaper templates, and also many pictures for you to get an idea of what we want on the newspaper. I have also attached our logo to use in the newspaper, and also a sample advertisement to what we are looking for.

The article that we would like to use on the front page is 1 document, and the other four (to use on the backside of the newspaper template) articles are attached as 1 document. This is a pretty simple project, but we do need you to use your creative side and come up with a spectacular project.

PLEASE DO NOT CHANGE THE WORDING IN THE ARTICLES!!!

• The design should capture our audiences attention and highlight the articles featured
• Layout should be neatly aligned, straight forward and not cluttered
• Text and Font are very important and should be legible and big enough to read. We are looking for something that is bold and gives the newsletter a look that stands out.
Updates

I have added a couple more pictures to use

THERE ARE WORDS THAT ARE BOLDED IN THE ORIGINAL DOCUMENT.  PLEASE LEAVE THE WORDS BOLDED, JUST AS THEY ARE IN THE DOCUMENT.  THANKS!!!!!

Please make sure all of the bolding is in the articles (This includes, the Headlines, the words in the articles, and also the whole sentence section.

Industry/Entity Type

It Company

Requirements
Must have
• PLEASE DO NOT CHANGE THE WORDING IN THE ARTICLES!!

ALL ARTICLES NEED TO BE ON NEWSLETTER (TOTAL OF 5 ARTICLES)

FRONT AND BACK, AND FULL COLOR.

```html
<!DOCTYPE html>
<html lang="en">
<head>
<meta charset="utf-8">
<title>Counseling News – Issue 1</title>
<link href="https://fonts.googleapis.com/css2?family=Anton&family=Roboto+Condensed:wght@400;700&family=Arimo:wght@400;700&display=swap" rel="stylesheet">
<style>
:root{
  --paper:#efe6da;
  --brown-dark:#3a1f0e;
  --brown:#5a3317;
  --brown-mid:#7a4a22;
  --yellow:#f7d417;
  --ink:#1d1a17;
  --white:#ffffff;
  --sidebar:#3b2414;
}
*{box-sizing:border-box;margin:0;padding:0}
html,body{width:1200px;height:776px;overflow:hidden;background:var(--paper)}
.sheet{position:absolute;left:0;top:0;width:1224px;height:792px;transform:scale(0.9804);transform-origin:0 0;background:var(--paper);font-family:"Roboto Condensed","Arial Narrow",sans-serif;color:var(--ink)}
.abs{position:absolute}
.page-divider{left:612px;top:0;width:1px;height:792px;background:#cdbfae}

/* masthead */
.masthead{left:15px;top:18px;width:597px;height:88px;background:linear-gradient(180deg,#6b3d1c 0%,var(--brown-dark) 100%)}
.masthead .issue{position:absolute;left:13px;top:7px;color:var(--white);font:400 10.5px "Arimo",sans-serif}
.masthead .title{position:absolute;left:40px;top:20px;font:400 56px/1 "Anton",sans-serif;letter-spacing:1.5px}
.title .c1{color:var(--yellow)}
.title .c2{color:var(--white)}
.masthead .tagline{position:absolute;right:18px;bottom:6px;color:var(--yellow);font:400 11px "Arimo",sans-serif}

.seal{left:415px;top:112px;width:152px;height:152px;border-radius:50%;background:#f6f2ec;border:10px solid #b7262c}

.lead-headline{left:58px;top:124px;width:360px;font:700 25px/26px "Roboto Condensed",sans-serif;color:var(--ink);white-space:nowrap}

.photo{background:linear-gradient(160deg,#8b6a4a 0%,#6d5a46 40%,#3e3226 100%)}
.lead-photo{left:50px;top:240px;width:350px;height:233px;border:1px solid #c9baa6}

.body{font-family:"Roboto Condensed","Arial Narrow",sans-serif;font-size:9.3px;line-height:10.3px;text-align:justify}
.body h4{font-style:italic;font-weight:700;font-size:9.3px;margin-top:10px;text-align:left}
.col1{left:50px;top:484px;width:172px}
.col2{left:234px;top:484px;width:172px}
.col3{left:420px;top:254px;width:176px}

.page-label{font:400 9px "Arimo",sans-serif;transform:rotate(-90deg);transform-origin:left top;white-space:nowrap;color:var(--ink)}
.label-1{left:14px;top:786px}
.label-2{left:626px;top:786px}

/* page 2 */
.mini-masthead{left:660px;top:18px;width:355px;height:27px;background:linear-gradient(180deg,#6b3d1c,var(--brown-dark))}
.mini-masthead .title{position:absolute;left:6px;top:1px;font:400 20px/1.2 "Anton",sans-serif;letter-spacing:0.5px}

.story-head{font:700 18px/22px "Roboto Condensed",sans-serif;color:var(--ink);white-space:nowrap;letter-spacing:-0.2px}
.weld-head{left:660px;top:62px;width:355px}
.weld-photo{left:660px;top:155px;width:170px;height:115px}
.weld-sentence{left:660px;top:276px;width:170px;font-weight:700}
.weld-body{left:842px;top:153px;width:173px}
.hartman-head{left:660px;top:348px;width:355px}
.hartman-c1{left:660px;top:442px;width:170px}
.hartman-c2{left:842px;top:442px;width:173px}

.ad{left:660px;top:565px;width:352px;height:207px;border:2px solid var(--brown-mid);background:var(--white)}
.ad .ask{position:absolute;left:0;right:0;top:14px;text-align:center;font:700 13px/1.3 "Arimo",sans-serif;color:var(--brown-dark)}
.ad .brand{position:absolute;left:30px;top:68px;display:flex;align-items:center;gap:14px}
.ad .brand-dot{width:46px;height:46px;border-radius:50%;background:var(--brown-mid)}
.ad .brand-name{font:700 27px/1.05 "Arimo",sans-serif;color:var(--brown-dark)}
.ad .sub{position:absolute;left:80px;right:0;top:130px;text-align:center;font:400 15px "Arimo",sans-serif;color:var(--brown-dark)}
.ad .url{position:absolute;left:4px;right:4px;bottom:4px;height:24px;background:linear-gradient(180deg,#6b3d1c,var(--brown-dark));color:var(--white);text-align:center;font:700 13px/24px "Arimo",sans-serif}

.sidebar{left:1020px;top:0;width:204px;height:792px;background:var(--sidebar)}
.side-head{color:var(--yellow);font:400 15.5px/16.5px "Roboto Condensed",sans-serif;white-space:nowrap}
.kean-head{left:1034px;top:36px;width:180px}
.side-body{color:var(--white);font-size:8.9px;line-height:10.6px;text-align:left}
.kean-body{left:1034px;top:118px;width:178px}
.side-rule{left:1020px;top:346px;width:204px;height:1px;background:#6e5240}
.conway-head{left:1034px;top:352px;width:180px}
.conway-photo{left:1034px;top:445px;width:162px;height:136px;background:linear-gradient(160deg,#ffffff 0%,#e8e3dd 55%,#a06a38 100%)}
.conway-body{left:1034px;top:592px;width:178px}
</style>
</head>
<body>
<div class="sheet">
  <div class="abs page-divider"></div>

  <!-- Front page -->
  <header class="abs masthead">
    <span class="issue">Year 1 Number 1 - Tuesday 5th December 2013</span>
    <div class="title"><span class="c1">COUNSELING</span><span class="c2">NEWS</span></div>
    <span class="tagline">Lorem ipsum dolor sit amet</span>
  </header>

  <div class="abs seal" role="img" aria-label="Agency seal"></div>

  <h1 class="abs lead-headline">Dr. Lyle Warren, M.D., President<br>of the American Society<br>of Pain Care (ASPC)<br>is under investigation by the N.D.C.B</h1>

  <div class="abs photo lead-photo" role="img" aria-label="Photo of officers and investigators outside a brick clinic building"></div>

  <div class="abs body col1">
    <p>The recent revelation that Dr.Lyle Warren, MD, <b>President of the American Society of Pain Care (ASPC)</b>, is under investigation by the <b>National Drug Control Bureau (NDCB)</b> likely caught most of the pain medicine community by surprise. The NDCB searched Dr. Warren's Evergreen Pain Clinic in Salt Lake City.</p>
    <p>Dr. Warren, a prominent expert in the use of analgesic drugs, acknowledged that former patients of his clinic have died of narcotic overdoses, according to a recent article in the Lakeshore Daily Herald.</p>
    <h4>A Show of Support</h4>
    <p>Many of Dr. Warren's colleagues reacted to the news with <b>surprise</b> and words of support for the leading pain specialist, who regularly <b>lectures on preventing opioid abuse</b>, and whose <b><u>Opioid Safety Screen</u> to identify patients most likely to abuse opioids is used by legions of doctors.</b></p>
    <p>Gordon J. Falcone, MD, director of pain man-</p>
  </div>

  <div class="abs body col2">
    <p>agement at Northbrook-Hale Medical Center in Lebanon, N.H said. "He's an exemplary provider. He cares about his patients and knows as much as anyone about treating patients with opioids."</p>
    <p>Dr. Falcone stressed that physicians at Academic Centers, like Dr. Warren and himself, <b>see the highest-risk patients</b>. This group includes pain patients with a history of substance abuse and mental health disorders who are at the greatest risk for overdose and suicide.</p>
    <p>"We do our best to identify patients with other problems who shouldn't be treated with opioids, but we all recognize the <b>best systems are imperfect</b>," said Dr. Falcone. <b>"It's still possible for people to slip through the cracks."</b></p>
    <p>Paul Sayer, spokesman for the <b>ASPC, responded to the investigation</b> by releasing an official statement <b>"Physicians in the ASPC</b> treat patients who have suffered horrific injuries or are terminally ill and in great pain.</p>
  </div>

  <div class="abs body col3">
    <p>A small percentage of those terribly suffering <b>patients die</b>—not as a result of appropriate medical treatment, but in spite of it."</p>
    <p><b>The ASPC's statement continues:</b> "As a society, we must care for the millions of people who suffer from pain, while preventing those same patients from ending their lives by overusing their medications. <b>Dr. Warren</b> is one of <b>the most highly respected physicians in the field and has worked tirelessly to prevent the overprescribing and misuse of opioids as part of a pain treatment regimen."</b></p>
    <h4><u>Comment From Dr. Lyle Warren</u></h4>
    <p><b>"The goal is safe prescribing</b>, but that doesn't happen in a vacuum. Health care involves a complex set of relationships, and the use of controlled medications to treat pain touches on many of them: <b>the patient's responsibility</b>, the health care plan (assuming there is one), community resources, the physician's level of experience, etc. <b>Physicians make choices about prescribing controlled medication in the moment</b>, based on numerous factors, including the patient's individual medical history.</p>
    <p>"So when we are talking about <b>'safer' prescribing</b>, we are really talking about addressing <b>all</b> of these things and not just the drug selected or the amount prescribed. <b>The pain medicine community</b> must focus on <b>Minimizing risk while still meeting the needs of patients</b>; this is what I have and will continue to push for as a researcher and educator in this field."</p>
    <p>"After Three Years, NDCB Investigation of Pain Doctor Lacks Conclusions" by Dana Harlow-Simms.</p>
  </div>

  <div class="abs page-label label-1">Counseling News -Page 1</div>

  <!-- Back page -->
  <div class="abs mini-masthead">
    <div class="title"><span class="c1">COUNSELING</span><span class="c2">NEWS</span></div>
  </div>

  <h2 class="abs story-head weld-head">Daniel W. Weld, MD Destin, FL,<br>guilty of Dispensing a Controlled Substance;<br>Resulting in Death; Conspiracy to Distribute, Di-<br>spense Controlled Substance</h2>
  <div class="abs photo weld-photo" role="img" aria-label="Press photo of a doctor speaking to reporters beside an officer"></div>
  <div class="abs body weld-sentence">
    <p>Sentence: Concurrent life sentences on the three death-results convictions. He was ordered to pay $59,239.32 in restitution. Weld's convictions and sentences were affirmed on appeal.</p>
  </div>
  <div class="abs body weld-body">
    <p>Daniel Weld, MD of Destin, FL, was found guilty in US District Court, Northern District of Florida, of 3 counts arising from his unlawful dispensing of controlled substances. Three counts of conviction charged that a patient's death resulted from the use of controlled substances dispensed by Weld. According to court documents, between November, 2002 and May, 2007, Weld prescribed controlled substances, By prescribing these controlled substances, Weld was acting outside the usual course of professional practice. <b>Weld Failed to medically monitor his patients or address the abuse of the controlled substances he prescribed to his patients.</b></p>
  </div>

  <h2 class="abs story-head hartman-head">Kevin Lee Hartman, DO, Deer Park, WA Guilty of<br>Prescribing Schedule II controlled substances for<br>other than a legitimate medical purpose and<br>outside the usual course of professional practice</h2>
  <div class="abs body hartman-c1">
    <p><b>Sentence: Hartman was sentenced to nine months incarceration, followed by three years supervised release. Hartman was also ordered to complete 240 hours of community service. He also agreed to forfeit his medical license and registration number.</b></p>
    <p>Kevin Lee Hartman, DO, age 69, of Deer Park, WA, pled guilty in U.S. District Court, Eastern</p>
  </div>
  <div class="abs body hartman-c2">
    <p>District of Washington; to one count of prescribing Schedule II controlled substances for other than a legitimate medical purpose and outside the usual course of professional practice. According to the court documents, Hartman prescribed Schedule II controlled substances, including Methadone and Oxycodone, to a patient despite Hartman being informed that <b>the patient was abusing drugs</b>.</p>
  </div>

  <div class="abs ad">
    <div class="ask">Can You Afford Not To Use<br>Brightway Counseling??</div>
    <div class="brand"><span class="brand-dot"></span><span class="brand-name">Brightway<br>Counseling</span></div>
    <div class="sub">a pro active addiction center</div>
    <div class="url">www.brightwaycounseling.example</div>
  </div>

  <div class="abs page-label label-2">Counseling News -Page 2</div>

  <aside class="abs sidebar"></aside>
  <h3 class="abs side-head kean-head">Gerard Kean, MD,<br>Highland Park, IL,<br>guilty of Reckless Conduct</h3>
  <div class="abs body side-body kean-body">
    <p><b>Sentence: 12 months incarceration (stayed) and 30 months probation. He was also ordered to pay $3000 contribution to Lakeside Bar Foundation; $1000 contribution to Lakeside Children's Advocacy Center; and pay $1000 contribution to Community Watch Fund.</b></p>
    <p>Gerard Kean, MD of Highland Park, IL, pled guilty in Federal Court, to one count Reckless Conduct. According to court documents, between June 1, 2006 and November 2, 2008, Kean caused permanent disability to a patient of his by regularly prescribing large amounts of narcotics. Kean prescribed, Oxycodone, to his patient <b>after he had two negative urine screens</b>, thereby indicating he was <b>not using prescribed narcotics</b> wherein the patient then became <b>Addicted and Dependent on the narcotics</b>.</p>
  </div>
  <div class="abs side-rule"></div>
  <h3 class="abs side-head conway-head">Caroline Ann Conway, MD,<br>Littleton, CO,<br>guilty of Possession of a<br>Schedule II Controlled<br>Substance</h3>
  <div class="abs conway-photo" role="img" aria-label="Photo of a stethoscope beside a wooden gavel"></div>
  <div class="abs body side-body conway-body">
    <p><b>Sentence: Conway was sentenced to one year probation.</b></p>
    <p>Caroline Ann Conway, MD, age 45, of Littleton, CO, pled guilty in First Judicial District of Colorado to one count of the issuance of controlled substance prescriptions without medical necessity or not in the course of usual medical practice. According to the court documents, Conway prescribed a controlled substance, specifically oxycodone, to a <b>known drug dependent</b> patient, outside the usual course of medical practice and not for legitimate medical purposes.</p>
  </div>
</div>
</body>
</html>
```